Business card design needed

My company specialises in carpentry and building services.
Based in Brisbane QLD
We also do:
property maintenance
plastering
painting
tiling
property maintenance

Industry/Entity Type

Carpentry

Contact Information for Business Card

RT Services QLD
Mark 0412583047
Dean 0493217586

```html
<!DOCTYPE html>
<html lang="en">
<head>
<meta charset="utf-8">
<title>RT Services QLD – Business Cards</title>
<link rel="stylesheet" href="https://fonts.googleapis.com/css2?family=Open+Sans:wght@400;600;700&display=swap">
<style>
  :root {
    --page-bg: #f1f1f1;
    --blue-deep: #2a4ea3;
    --blue-light: #5499d6;
    --wall-dark: #2f3032;
    --wall-mid: #3a3b3e;
    --text-white: #ffffff;
    --text-grey: #9a9a9a;
    --text-soft: #d6d6d6;
    --brand-grey: #8d8d8d;
  }
  * { margin: 0; padding: 0; box-sizing: border-box; }
  html, body {
    width: 1200px; height: 1000px; overflow: hidden;
    background: var(--page-bg);
    font-family: "Open Sans", Arial, sans-serif;
  }
  .stage { position: relative; width: 1200px; height: 1000px; }
  .card {
    position: absolute; width: 630px; height: 365px; overflow: hidden;
    box-shadow: 0 10px 18px rgba(0,0,0,0.35);
  }
  .card--dean { left: 135px; top: 140px; }
  .card--mark { left: 448px; top: 525px; }
  .card__art { position: absolute; inset: 0; width: 100%; height: 100%; }
  .brand {
    position: absolute; left: 38px; top: 58px;
    color: var(--text-white); font-weight: 700; font-size: 32px;
    letter-spacing: 1px; text-transform: uppercase; line-height: 40px;
  }
  .brand__region {
    position: absolute; left: 42px; top: 102px;
    color: var(--brand-grey); font-size: 24px; font-weight: 400; line-height: 30px;
  }
  .contact {
    position: absolute; right: 24px; top: 84px; text-align: right;
    color: var(--text-white);
  }
  .contact__name { font-size: 23px; font-weight: 600; line-height: 30px; margin-bottom: 10px; letter-spacing: 0.5px; }
  .contact__line { font-size: 18px; line-height: 24px; letter-spacing: 0.6px; }
  .contact__legal { font-size: 12.5px; line-height: 16px; color: var(--text-soft); margin-top: 4px; letter-spacing: 0.4px; }
  .services { position: absolute; left: 44px; bottom: 34px; }
  .services__main { color: var(--text-white); font-size: 20px; font-weight: 600; line-height: 26px; letter-spacing: 0.3px; }
  .services__list { color: var(--text-grey); font-size: 19px; line-height: 26px; letter-spacing: 0.3px; }
</style>
</head>
<body>
<main class="stage">

  <section class="card card--dean">
    <svg class="card__art" viewBox="0 0 630 365" preserveAspectRatio="none" aria-hidden="true">
      <defs>
        <linearGradient id="skyDean" x1="0" y1="0" x2="1" y2="0">
          <stop offset="0" stop-color="var(--blue-deep)"/>
          <stop offset="1" stop-color="var(--blue-light)"/>
        </linearGradient>
        <linearGradient id="wallDean" x1="0" y1="0" x2="1" y2="1">
          <stop offset="0" stop-color="var(--wall-mid)"/>
          <stop offset="1" stop-color="var(--wall-dark)"/>
        </linearGradient>
      </defs>
      <rect width="630" height="365" fill="url(#skyDean)"/>
      <polygon role="img" aria-label="Textured dark concrete wall with blue paint flecks"
        fill="url(#wallDean)" points="0,255 630,120 630,365 0,365"/>
    </svg>
    <div class="brand">RT Services</div>
    <div class="brand__region">QLD</div>
    <div class="contact">
      <div class="contact__name">Dean</div>
      <div class="contact__line">0493217586</div>
      <div class="contact__line">dean.rtsqld@rtmail.com</div>
      <div class="contact__line">www.rtsqld.com.au</div>
      <div class="contact__legal">BSA license no:1304718<br>ABN: 61482093517</div>
    </div>
    <div class="services">
      <div class="services__main">Carpentry and Building Services</div>
      <div class="services__list">Property Maintenance / Plastering/ Painting/ Tiling</div>
    </div>
  </section>

  <section class="card card--mark">
    <svg class="card__art" viewBox="0 0 630 365" preserveAspectRatio="none" aria-hidden="true">
      <defs>
        <linearGradient id="skyMark" x1="0" y1="0" x2="1" y2="0">
          <stop offset="0" stop-color="var(--blue-deep)"/>
          <stop offset="1" stop-color="var(--blue-light)"/>
        </linearGradient>
        <linearGradient id="wallMark" x1="0" y1="0" x2="1" y2="1">
          <stop offset="0" stop-color="var(--wall-mid)"/>
          <stop offset="1" stop-color="var(--wall-dark)"/>
        </linearGradient>
      </defs>
      <rect width="630" height="365" fill="url(#skyMark)"/>
      <polygon role="img" aria-label="Textured dark concrete wall with blue paint flecks"
        fill="url(#wallMark)" points="0,255 630,120 630,365 0,365"/>
    </svg>
    <div class="brand">RT Services</div>
    <div class="brand__region">QLD</div>
    <div class="contact">
      <div class="contact__name">Mark</div>
      <div class="contact__line">0412583047</div>
      <div class="contact__line">mark.rtsqld@rtmail.com</div>
      <div class="contact__line">www.rtsqld.com.au</div>
      <div class="contact__legal">BSA license no:1304718<br>ABN: 61482093517</div>
    </div>
    <div class="services">
      <div class="services__main">Carpentry and Building Services</div>
      <div class="services__list">Property Maintenance / Plastering/ Painting/ Tiling</div>
    </div>
  </section>

</main>
</body>
</html>
```